Castastrophe General Contractor needs leave behind for sales

Will respond quickly to designer inquires
Fast winning selection
Will notify all of winning selection

Catastrophe Restoration General Contractor offering specialized services to the insurance industry. Sales meeting leave behind flyer for presentation to insurance agents. We would like for agents to refer policyholders to our company for complete residential and commercial restoration projects.

Some copy uploaded for reference. 5.5" x 8.5" approx - double sided color w/ sales business card reproduced on back side. Approved / Preferred Contractor for Brightshield, Vantacover, KRPQ & Fenlo insurance companies.

Larkmoor Company is a general contractor specialized in the restoration industry for both residential and commercial properties.
We have incorporated the best technology tools and partnered with a network of industry professionals across the country to provide the most efficient and comprehensive service available.
Website under construction: www.thelarkmoorcompany.example

Target Market(s)

Insurance Sale Agents

Industry/Entity Type

Residential

Requirements
Must have
• Brightshield, Vantacover & KRPQ & Halvey Dresmit logos. Space to reproduce business card on back.. Looking for concept deign where we can work w/ local designer if necessary to finalize. Open to different sized flyer dependent on design.

```html
<!DOCTYPE html>
<html lang="en">
<head>
<meta charset="utf-8">
<title>Larkmoor Company – Agent Support Flyer</title>
<link rel="stylesheet" href="https://fonts.googleapis.com/css2?family=Source+Sans+3:ital,wght@0,400;0,600;0,700;1,400&display=swap">
<style>
  :root {
    --ink: #1c1b1b;
    --card: #262324;
    --orange: #f7a81b;
    --gold: #f3b12a;
    --white: #ffffff;
    --navy: #1f3f7a;
    --text: #1e1e1e;
  }
  * { margin: 0; padding: 0; box-sizing: border-box; }
  html, body { width: 776px; height: 1200px; overflow: hidden; background: var(--white); }
  body { font-family: "Source Sans 3", Arial, sans-serif; color: var(--text); position: relative; }

  .header-band {
    position: absolute; left: 0; top: 0; width: 776px; height: 112px;
    background: var(--ink); color: var(--white);
    padding: 14px 22px; font-size: 30px; line-height: 38px;
  }
  .accent-strip { position: absolute; left: 0; top: 112px; width: 776px; height: 18px; }

  .intro { position: absolute; left: 24px; top: 170px; font-size: 25px; line-height: 30px; }
  .services { position: absolute; left: 24px; top: 268px; font-size: 25px; line-height: 30px; }
  .services h2 { font-weight: 400; font-size: 25px; }
  .services ul, .benefits ul { list-style: none; }
  .services li::before, .benefits li::before { content: "• "; }

  .benefits { position: absolute; left: 24px; top: 404px; font-size: 18px; line-height: 22.6px; }
  .benefits h3 { font-weight: 400; font-size: 19px; margin-bottom: 4px; }

  .approved-banner { position: absolute; left: 0; top: 772px; width: 448px; height: 62px; }
  .approved-banner svg { position: absolute; left: 0; top: 0; }
  .approved-banner span {
    position: absolute; left: 24px; top: 9px; font-size: 33px; color: var(--ink);
  }

  .partner-grid { position: absolute; left: 16px; top: 852px; width: 262px; height: 216px; }
  .partner-grid svg { position: absolute; left: 0; top: 0; }
  .partner-name { position: absolute; font-weight: 700; font-size: 17px; line-height: 20px; white-space: nowrap; }

  .business-card {
    position: absolute; left: 284px; top: 876px; width: 492px; height: 244px;
    background: var(--card); border-top: 3px solid var(--gold);
  }
  .card-tagline { position: absolute; left: 22px; top: 20px; font-style: italic; color: var(--gold); font-size: 19px; }
  .card-phone { position: absolute; left: 22px; top: 128px; color: var(--white); font-size: 42px; line-height: 50px; }
  .card-email { position: absolute; left: 22px; top: 182px; color: var(--gold); font-size: 22px; }

  .brand-mark { position: absolute; display: flex; align-items: center; gap: 8px; }
  .brand-mark i { display: block; width: 20px; height: 20px; background: var(--gold); }
  .brand-mark b { font-weight: 600; color: var(--white); letter-spacing: 0.5px; white-space: nowrap; }
  .card-brand { right: 24px; top: 40px; }
  .card-brand b { font-size: 15px; }

  .web-strip {
    position: absolute; left: 284px; top: 1120px; width: 492px; height: 58px;
    background: var(--orange); color: var(--ink); font-size: 30px; white-space: nowrap;
    display: flex; align-items: center; justify-content: center;
  }
  .footer-brand-block { position: absolute; left: 0; top: 1076px; width: 284px; height: 124px; background: var(--ink); }
  .footer-brand { left: 36px; top: 48px; }
  .footer-brand b { font-size: 20px; }
</style>
</head>
<body>
  <header class="header-band">Catastrophe Restoration General Contractor<br>offering specialized services to the insurance industry.</header>
  <svg class="accent-strip" viewBox="0 0 776 18" aria-hidden="true">
    <rect width="776" height="18" fill="#f7a81b"/>
    <polygon points="676,0 776,0 776,18 700,18" fill="#1c1b1b"/>
  </svg>

  <section class="intro">
    <p>Preferred Contractor Agent Support</p>
    <p>Providing claims support during and after a CAT event</p>
  </section>

  <section class="services">
    <h2>Agent Support Services</h2>
    <ul>
      <li>Guaranteed next day inspections from time of notification</li>
      <li>Damage status reporting directly back to Agent</li>
      <li>Assist policy holder in filing claim to CAT desk</li>
    </ul>
  </section>

  <section class="benefits">
    <h3>Agent Benefits:</h3>
    <ul>
      <li>Greater Satisfaction, Increased Retention</li>
      <li>Increase policyholder satisfaction</li>
      <li>Demonstrate a greater commitment to customer satisfaction</li>
      <li>Follow up on outcome beyond the closing of a claim</li>
      <li>Enhanced Efficiency</li>
      <li>Increase efficiency in moving from claim to restoration completion</li>
      <li>“In-house” systems closely linked to the insurer or administrator</li>
      <li>Shorten the timeline from claims settlement to finished repairs</li>
      <li>Increased Quality Control</li>
      <li>Pre-screened and credentialed for license, insurance, and financial stability</li>
      <li>Monitored performance and control standards for higher-quality outcomes</li>
      <li>Background verification on all staff and field representatives</li>
    </ul>
  </section>

  <div class="approved-banner">
    <svg width="448" height="62" viewBox="0 0 448 62" aria-hidden="true">
      <polygon points="0,0 418,0 448,31 418,62 0,62" fill="#f7a81b"/>
    </svg>
    <span>Approved Contractor For.....</span>
  </div>

  <div class="partner-grid">
    <svg width="262" height="216" viewBox="0 0 262 216" role="img" aria-label="Partner and certification badges">
      <rect x="2" y="4" width="40" height="74" rx="4" fill="#1f3f7a"/>
      <circle cx="72" cy="24" r="20" fill="#3c78c3"/>
      <circle cx="118" cy="24" r="20" fill="#3c78c3"/>
      <circle cx="164" cy="24" r="20" fill="#3c78c3"/>
      <rect x="52" y="58" width="22" height="26" fill="#e85a8a"/>
      <circle cx="140" cy="180" r="20" fill="#2a3b7a"/>
    </svg>
    <span class="partner-name" style="left:196px;top:14px;color:#1f3f7a">KRPQ</span>
    <span class="partner-name" style="left:80px;top:60px;color:#333;font-size:15px">Halvey<br>Dresmit</span>
    <span class="partner-name" style="left:2px;top:104px;color:#1f3f7a;font-size:15px">Brightshield</span>
    <span class="partner-name" style="left:118px;top:100px;color:#1a7a5a">Fenlo</span>
    <span class="partner-name" style="left:2px;top:168px;color:#1f5fa8;font-size:17px">Vantacover</span>
  </div>

  <section class="business-card">
    <p class="card-tagline">Claim Support after a CAT event</p>
    <div class="brand-mark card-brand"><i></i><b>LARKMOOR COMPANY</b></div>
    <p class="card-phone">(800) 555-0186</p>
    <p class="card-email">info@larkmoorcompany.example</p>
  </section>
  <div class="web-strip">www.larkmoorcompany.example</div>

  <div class="footer-brand-block">
    <div class="brand-mark footer-brand"><i></i><b>LARKMOOR COMPANY</b></div>
  </div>
</body>
</html>
```